Thank You Card design for a federal credit union

I am looking to have a thank you card designed.
Specs:
Flat size of 9.5"x6.5" folds to final size of 4.75"x6.5", it will print full color on the front and back. Below, you will see their logo, which needs to print on the inside of the folded card. I also attached images of their current card. They would like to keep the blue color but are open to design on the front. This is a Federal Credit Union, so please make the design, modern and professional. Below is the text that needs to print below the logo on the inside of the card. The text and logo will print below the fold on the inside, leave the top portion (above the panel) white.
Inside text:
Our Members are the foundation of our Credit Union. We sincerely thank you for your loyalty, your business and the opportunity to serve you.
Target Market(s)
Clients of a federal credit union
Industry/Entity Type
Union
Requirements
Must have
- a simple, professional, and modern feel. "Thank You for your business" must be on the front section in some variation.
Should not have
- nothing flashy or too many colors. keep it simple

```html
<!DOCTYPE html>
<html lang="en">
<head>
<meta charset="UTF-8">
<title>Thank You Card</title>
<link rel="stylesheet" href="https://fonts.googleapis.com/css2?family=Cinzel:wght@400;700&family=Great+Vibes&display=swap">
<style>
  :root {
    --paper: #ffffff;
    --navy-deep: #14151f;
    --navy: #1a2238;
    --blue-glow: #1f6ec2;
    --blue-mid: #1b3f75;
    --ink-light: #ffffff;
  }
  html, body {
    margin: 0;
    padding: 0;
    width: 813px;
    height: 1200px;
    overflow: hidden;
    background: var(--paper);
  }
  .card {
    position: relative;
    width: 813px;
    height: 1200px;
    background: var(--paper);
  }
  .card__inside-top {
    position: absolute;
    left: 0;
    top: 0;
    width: 813px;
    height: 594px;
    background: var(--paper);
  }
  .card__front {
    position: absolute;
    left: 0;
    top: 594px;
    width: 813px;
    height: 606px;
    overflow: hidden;
    background:
      radial-gradient(ellipse 620px 420px at 50% 0%, var(--blue-glow) 0%, var(--blue-mid) 35%, var(--navy) 70%, var(--navy-deep) 100%);
    color: var(--ink-light);
  }
  .front__intro {
    position: absolute;
    left: 0;
    width: 100%;
    top: 84px;
    text-align: center;
    font-family: "Cinzel", serif;
    font-weight: 700;
    font-size: 20px;
    letter-spacing: 0.3px;
    margin: 0;
  }
  .front__headline {
    margin: 0;
    font-family: "Great Vibes", cursive;
    font-weight: 400;
  }
  .front__headline-thank,
  .front__headline-you {
    position: absolute;
    font-size: 160px;
    line-height: 1;
    white-space: nowrap;
  }
  .front__headline-thank {
    left: 100px;
    top: 170px;
  }
  .front__headline-you {
    left: 455px;
    top: 255px;
  }
  .front__closing {
    position: absolute;
    left: 0;
    width: 100%;
    top: 482px;
    text-align: center;
    font-family: "Cinzel", serif;
    font-weight: 400;
    font-size: 25px;
    letter-spacing: 0.5px;
    margin: 0;
  }
</style>
</head>
<body>
  <main class="card">
    <section class="card__inside-top" aria-label="Inside panel, left blank"></section>
    <section class="card__front">
      <p class="front__intro">WE WOULD LIKE TO THANK YOU</p>
      <h1 class="front__headline">
        <span class="front__headline-thank">Thank</span>
        <span class="front__headline-you">You</span>
      </h1>
      <p class="front__closing">FOR YOUR BUSINESS</p>
    </section>
  </main>
</body>
</html>
```